Birchline Heating & Air

I need a business card made for my company. I would like my new logo for Birchline Heating and Air on the front and my Garage Door on the back.
Front to say -Heating & Air Conditioning , Mini Splits and Heat Pumps, Hydronic In-Floor Heat. Locally Owned and Operated! Licensed, Boned and Insured. Free Estimates on new equipment. 715-408-2159
BGD Back Card, change phone# to 651-374-5810. Remove Commercial and residential and fully sticked vans lines.

```html
<!DOCTYPE html>
<html lang="en">
<head>
<meta charset="utf-8">
<title>Birchline Heating &amp; Air — Business Card</title>
<link href="https://fonts.googleapis.com/css2?family=Montserrat:wght@500;600;800;900&display=swap" rel="stylesheet">
<style>
  :root{
    --bg:#2b2b2d;
    --white:#ffffff;
    --brand-blue:#17528a;
    --brand-red:#e2301f;
    --text-light:#ffffff;
  }
  *{box-sizing:border-box;margin:0;padding:0}
  html,body{width:1200px;height:900px;overflow:hidden;background:var(--bg);font-family:"Montserrat",sans-serif}
  .canvas{position:relative;width:1200px;height:900px}
  .card{position:absolute;left:250px;width:700px;height:400px;border-radius:24px;overflow:hidden;background:var(--white);box-shadow:0 12px 30px rgba(0,0,0,.45)}
  .card--front{top:40px}
  .card--back{top:470px}
  .card svg.shapes{position:absolute;inset:0;width:100%;height:100%}

  /* front */
  .front-logo{position:absolute;left:0;right:0;top:42px;text-align:center}
  .front-logo__name{font-size:72px;font-weight:900;color:var(--brand-red);letter-spacing:1px;line-height:1}
  .front-logo__sub{font-size:34px;font-weight:900;color:var(--brand-blue);letter-spacing:2px;margin-top:6px}
  .front-services{position:absolute;left:0;right:0;top:200px;text-align:center;color:var(--text-light);font-weight:600;font-size:19px;line-height:36px;white-space:nowrap}
  .bullet{color:var(--brand-red);margin:0 6px}
  .front-offer{position:absolute;left:0;right:0;top:334px;height:66px;display:flex;align-items:center;justify-content:center;color:var(--text-light);font-weight:800;font-size:24px;letter-spacing:.5px;white-space:nowrap}

  /* back */
  .back-logo{position:absolute;right:44px;top:70px;display:flex;align-items:center;gap:14px}
  .back-logo__mark{width:26px;height:26px;background:var(--brand-red)}
  .back-logo__name{font-size:30px;font-weight:900;color:var(--brand-blue);letter-spacing:1px;line-height:1.1}
  .save-ribbon{position:absolute;left:34px;top:200px;color:var(--text-light);font-weight:800;font-size:27px;letter-spacing:1px;white-space:nowrap}
  .contact-list{position:absolute;left:34px;top:268px;list-style:none;color:var(--text-light);font-weight:500;font-size:17px;white-space:nowrap}
  .contact-list li{display:flex;align-items:center;gap:12px;height:34px}
  .contact-list svg{width:15px;height:15px;fill:var(--brand-red)}
  .service-list{position:absolute;left:385px;top:298px;list-style:none;color:var(--text-light);font-weight:500;font-size:18px;line-height:29px;white-space:nowrap}
  .service-list .bullet{margin:0 6px 0 0}
</style>
</head>
<body>
<main class="canvas">

  <section class="card card--front" aria-label="Card front">
    <svg class="shapes" viewBox="0 0 700 400" preserveAspectRatio="none" aria-hidden="true">
      <rect x="0" y="185" width="700" height="150" fill="var(--brand-blue)"/>
      <rect x="0" y="330" width="700" height="4" fill="var(--white)"/>
      <rect x="0" y="334" width="700" height="66" fill="var(--brand-red)"/>
    </svg>
    <div class="front-logo">
      <div class="front-logo__name">BIRCHLINE</div>
      <div class="front-logo__sub">HEATING &amp; AIR</div>
    </div>
    <div class="front-services">
      <p><span class="bullet">•</span>Heating &amp; Air Conditioning <span class="bullet">•</span>Mini Splits and Heat Pumps</p>
      <p><span class="bullet">•</span>Hydronic In-Floor Heat</p>
      <p>Locally Owned and Operated! Licensed, Boned and Insured.</p>
    </div>
    <div class="front-offer">FREE ESTIMATES ON NEW EQUIPMENT. 715-408-2159</div>
  </section>

  <section class="card card--back" aria-label="Card back">
    <svg class="shapes" viewBox="0 0 700 400" preserveAspectRatio="none" aria-hidden="true">
      <polygon points="0,240 700,292 700,400 0,400" fill="var(--brand-blue)"/>
      <polygon points="0,182 300,182 345,258 0,242" fill="var(--brand-red)"/>
    </svg>
    <div class="back-logo">
      <span class="back-logo__mark"></span>
      <span class="back-logo__name">BIRCHLINE<br>GARAGE DOOR</span>
    </div>
    <div class="save-ribbon">SAVE THIS CARD!</div>
    <ul class="contact-list">
      <li><svg viewBox="0 0 24 24"><path d="M6.6 10.8a15.1 15.1 0 0 0 6.6 6.6l2.2-2.2a1 1 0 0 1 1-.25 11.4 11.4 0 0 0 3.6.57 1 1 0 0 1 1 1V20a1 1 0 0 1-1 1A17 17 0 0 1 3 4a1 1 0 0 1 1-1h3.5a1 1 0 0 1 1 1c0 1.25.2 2.45.57 3.57a1 1 0 0 1-.25 1z"/></svg>651-374-5810</li>
      <li><svg viewBox="0 0 24 24"><path d="M2 5h20v14H2z M2 5l10 8 10-8" stroke="var(--brand-blue)" stroke-width="1.5"/></svg>hello@birchlinegaragedoor.com</li>
      <li><svg viewBox="0 0 24 24"><circle cx="12" cy="12" r="10"/></svg>www.BirchlineGarageDoor.com</li>
    </ul>
    <ul class="service-list">
      <li><span class="bullet">•</span>Same Day &amp; Emergency Service</li>
      <li><span class="bullet">•</span>All Major Brands</li>
      <li><span class="bullet">•</span>Locally Owned &amp; Operated</li>
    </ul>
  </section>

</main>
</body>
</html>
```